An anniversary gift for my girlfriend

My girlfriend and I have been dating for almost 2 years. We met online and this has afforded us the really unique opportunity to have the first words we said to each other (the whole conversation, in fact) preserved. We're moving in together in a few months and she doesn't know that I saved the conversation. I've been waiting for this to turn it into something we can hang in our new place.

The only phrase I want to use is:
"Well if you dislike people's knees then I think we'll get along famously"

It's an Nobody Leaves Before Midnight in Portland reference for the curious.

I want the poster to use the words themselves as the art; I'm thinking typography. I'd like it to match her aesthetic, she likes to wear Nora Vell and T. Brisk. Colors shouldn't be anything too "girly". Somewhere I'd like to include the date June 1, 2015. It shouldn't be a major piece of the poster though, just a way to denote the date.

It should fit (and be fully visible in) a 16x20 (inches) frame

Thanks in advance for the work!

Requirements
Must have
• Must use only the words: "Well if you dislike people's knees then I think we'll get along famously"
• I want this to be typography, so making the phrase the center of the poster and the art itself.

```html
<!DOCTYPE html>
<html lang="en">
<head>
<meta charset="utf-8">
<title>Knees — Anniversary Typography Poster</title>
<link rel="stylesheet" href="https://fonts.googleapis.com/css2?family=Jost:wght@500&family=Tinos&family=Playfair+Display:wght@700&display=swap">
<style>
  :root {
    --paper-light: #f7f7f7;
    --paper-edge: #e2e2e2;
    --quote-mark: #dcdcdc;
    --ink-date: #222222;
    --red: #e4302a;
    --cyan: #36b4cf;
    --yellow: #f2c200;
    --grey: #9b9b9b;
    --purple: #8c1b7f;
    --brown: #5b2b1d;
    --magenta: #d5156a;
    --green: #1f8b3b;
    --sky: #3cb4cc;
    --navy: #1e2a7b;
    --orange: #ee6a1c;
    --pink: #d65c9d;
  }
  * { margin: 0; padding: 0; box-sizing: border-box; }
  html, body { width: 1200px; height: 1148px; overflow: hidden; }
  body {
    background: radial-gradient(ellipse at 50% 40%, var(--paper-light) 0%, #eeeeee 55%, var(--paper-edge) 100%);
    position: relative;
  }
  .poster { position: absolute; inset: 0; }
  .quote-mark {
    position: absolute;
    font-family: "Playfair Display", Georgia, serif;
    font-weight: 700;
    font-size: 300px;
    line-height: 1;
    color: var(--quote-mark);
  }
  .quote-mark--open { left: 300px; top: 300px; }
  .quote-mark--close { left: 760px; top: 660px; }
  .phrase {
    position: absolute;
    left: 0; right: 0;
    top: 368px;
    text-align: center;
    font-family: "Jost", "Futura", sans-serif;
    font-weight: 500;
    font-size: 48px;
    line-height: 52px;
    text-transform: uppercase;
    letter-spacing: 0.5px;
  }
  .phrase__line { display: block; }
  .red { color: var(--red); }
  .cyan { color: var(--cyan); }
  .yellow { color: var(--yellow); }
  .grey { color: var(--grey); }
  .purple { color: var(--purple); }
  .brown { color: var(--brown); }
  .magenta { color: var(--magenta); }
  .green { color: var(--green); }
  .sky { color: var(--sky); }
  .navy { color: var(--navy); }
  .orange { color: var(--orange); }
  .pink { color: var(--pink); }
  .date {
    position: absolute;
    left: 0; right: 0;
    top: 738px;
    text-align: center;
    transform: translateX(-22px);
    font-family: "Tinos", "Times New Roman", serif;
    font-size: 15px;
    color: var(--ink-date);
    letter-spacing: 0.3px;
  }
</style>
</head>
<body>
  <main class="poster">
    <span class="quote-mark quote-mark--open" aria-hidden="true">&ldquo;</span>
    <span class="quote-mark quote-mark--close" aria-hidden="true">&rdquo;</span>
    <h1 class="phrase">
      <span class="phrase__line"><span class="red">Well</span> <span class="cyan">if</span> <span class="yellow">you</span></span>
      <span class="phrase__line"><span class="grey">dislike</span> <span class="purple">people's</span></span>
      <span class="phrase__line"><span class="brown">knees</span> <span class="magenta">then</span></span>
      <span class="phrase__line"><span class="green">I think</span></span>
      <span class="phrase__line"><span class="sky">we'll</span> <span class="navy">get</span></span>
      <span class="phrase__line"><span class="orange">along</span></span>
      <span class="phrase__line"><span class="pink">famously</span></span>
    </h1>
    <p class="date">JUNE 1, 2015</p>
  </main>
</body>
</html>
```